Counselling practice needs a Business Card Design

I need a business card design for a new counselling practice in Canberra, Australia. The name of the practice is Dr Henry Walsh, Counselling Services and the practice focuses on philosophical, narrative and existential counselling for individuals, couples and families. The final design should communicate professionalism, sophistication of analysis and psychological wholeness. The reverse side of the card should have an appointment reminder
Updates

Could the following qualifications also be included on card. BSc (Psychology), BA hons (Philosophy), PhD (Philosophy), Diploma of Community Counselling And the following affiliation Guild of Talk Therapists of Tasvale and District Inc. (GOTTTD) And my contact phone mobile phone number is 0455837190, and email is drhenrywalsh@tasvaletherapy.example for inclusion as well.

Thank you all who have put in a design so far. I just wanted to clarify some design points based on what you have submitted. 1. The Guild of Talk Therapists. Tasvale and District Inc. (GOTTTD) is an affiliation only. 'Member of the Guild of Talk Therapists. Tasvale and District Inc (GOTTTD)' should appear with the same prominence of a qualification. 2. The Post Graduate Diploma in Community Counselling is a quaification and should appear as 'PG Dip (Community Counselling)' after the other qualifications. 3. I am advertising myself as a counsellor so 'Dr Henry Walsh, Counselling Services' or 'Dr Henry Walsh, Counsellor' is the equivalent of the business name. After looking at some of the designs I prefer Dr Henry Walsh in sentence case rather than all capitals (DR HENRY WALSH). 4. 'Philosophical, narrative and existential counselling for individuals, couples and families' is the description of the type of counselling services and should appear on the card.

One further point. I have updated my email address for the card. It is now drhenrywalsh@tasvaletherapy.example

```html
<!DOCTYPE html>
<html lang="en">
<head>
<meta charset="utf-8">
<title>Dr Henry Walsh, Counselling Services — Business Card</title>
<link rel="stylesheet" href="https://fonts.googleapis.com/css2?family=Fira+Sans:wght@300;400&display=swap">
<style>
  :root {
    --paper: #ffffff;
    --aqua: #00ffff;
    --aqua-ink: #0ae8f0;
    --ink-light: #ffffff;
    --band-start: #d9dcdf;
    --band-end: #f4f5f6;
  }
  * { margin: 0; padding: 0; box-sizing: border-box; }
  html, body {
    width: 1200px;
    height: 857px;
    overflow: hidden;
    background: var(--paper);
  }
  .card {
    position: relative;
    width: 1200px;
    height: 857px;
    font-family: "Fira Sans", sans-serif;
    font-weight: 300;
    background: var(--paper);
    overflow: hidden;
  }
  .card__header {
    position: absolute;
    left: 0; top: 0;
    width: 100%;
    height: 375px;
    text-align: center;
    color: var(--aqua-ink);
  }
  .tagline { position: absolute; left: 0; width: 100%; line-height: 1; white-space: nowrap; }
  .tagline--lead { top: 46px; font-size: 64px; }
  .tagline--sub { top: 132px; font-size: 43.5px; }
  .tagline--amp { top: 203px; font-size: 40px; }
  .tagline--close { top: 253px; font-size: 58px; }

  .divider-band {
    position: absolute;
    left: 0; top: 375px;
    width: 100%;
    height: 16px;
    background: linear-gradient(to right, var(--band-start), var(--band-end));
  }
  .card__details {
    position: absolute;
    left: 0; top: 391px;
    width: 100%;
    height: 466px;
    background: var(--aqua);
    color: var(--ink-light);
  }
  .practitioner-name {
    position: absolute;
    left: 92px; top: 63px;
    font-size: 44px;
    font-weight: 300;
    line-height: 1;
    white-space: nowrap;
  }
  .credentials {
    position: absolute;
    left: 92px; top: 134px;
    font-size: 28.5px;
    line-height: 43px;
    white-space: nowrap;
  }
  .contact {
    position: absolute;
    left: 0; top: 338px;
    width: 100%;
    text-align: center;
    font-size: 31px;
    line-height: 44px;
    font-style: normal;
  }
</style>
</head>
<body>
  <main class="card">
    <header class="card__header">
      <p class="tagline tagline--lead">Counselling Services and the practice</p>
      <p class="tagline tagline--sub">focuses on philosophical, narrative</p>
      <p class="tagline tagline--amp">&amp;</p>
      <p class="tagline tagline--close">existential counselling</p>
    </header>
    <div class="divider-band"></div>
    <section class="card__details">
      <h1 class="practitioner-name">Dr Henry Walsh</h1>
      <p class="credentials">
        BSc (Psychology), BA hons (Philosophy), PhD (Philosophy),<br>
        PG Dip (Community Counselling). Member of the Guild of Talk Therapists.<br>
        Tasvale and District Inc (GOTTTD)
      </p>
      <address class="contact">
        0455837190<br>
        drhenrywalsh@tasvaletherapy.example
      </address>
    </section>
  </main>
</body>
</html>
```